Info Graphic about Maple Ridge Restaurant

This info graphic should detail all releavent details about Maple Ridge, such as opening hours, accepted payment methods, home delivery areas etc. please refer attached word document for details.

Also attached a pdf with old info graphic.

IMPORTANT:. Given there is lot of text, I expect the designer to make this interesting. This will be printed in A1 and also A4
Also, I need this in both Portrait and landscape designs.

Industry/Entity Type

Hospitality

Font styles to use
Serif
Sans Serif
Decorative
Script
Other font styles liked:
• I let designer choose

Colors

Designer to choose colors to be used in the design.

Requirements
Must have
• Refer attached word doc
Nice to have
• Refer attached word doc
Should not have
• Refer attached word doc

```html
<!DOCTYPE html>
<html lang="en">
<head>
<meta charset="utf-8">
<title>Maple Ridge Indian Restaurant – Info Sheet</title>
<link href="https://fonts.googleapis.com/css2?family=Roboto:wght@300;400;500;700;900&family=Roboto+Condensed:wght@700&display=swap" rel="stylesheet">
<style>
:root{
  --red:#e8232b;
  --orange:#f26a22;
  --olive:#c3b52f;
  --cream:#fdf9e4;
  --mist:#f3f4f8;
  --ink:#222;
}
*{margin:0;padding:0;box-sizing:border-box}
html,body{width:849px;height:1200px;overflow:hidden;background:#fff}
body{font-family:'Roboto',sans-serif;color:var(--ink)}
.sheet{position:relative;width:849px;height:1200px;overflow:hidden}
.abs{position:absolute}
.stripe{position:absolute;left:0;width:849px;height:5px;
  background:linear-gradient(90deg,var(--olive) 0 14%,var(--orange) 14% 28%,var(--red) 28% 45%,var(--olive) 45% 58%,var(--orange) 58% 72%,var(--red) 72% 88%,var(--orange) 88%)}
.heading{font-family:'Roboto Condensed',sans-serif;font-weight:700;text-transform:uppercase}

.header{top:0;height:96px;width:849px;background:#fff}
.brand{left:38px;top:22px;display:flex;align-items:center;gap:12px}
.brand-dot{width:40px;height:40px;border-radius:50%;background:var(--red)}
.brand-name{font-weight:900;font-size:42px;color:var(--red);letter-spacing:.3px}

.location{top:101px;height:195px;width:849px;background:#fff}
.map{left:0;top:0;width:400px;height:195px;background:linear-gradient(135deg,#ecebe6,#dcdad4)}
.loc-title{left:417px;top:16px;font-size:29px;color:var(--red)}
.loc-text{left:417px;top:55px;font-size:13px;line-height:17px}
.contact{top:152px;display:flex;align-items:center;gap:8px;font-size:17px}
.icon{width:29px;height:29px;border-radius:50%;background:var(--orange);display:flex;align-items:center;justify-content:center}

.hours{top:302px;height:152px;width:849px;background:var(--cream)}
.clock{left:62px;top:14px}
.hours-title{left:222px;top:9px;font-size:36px;color:var(--olive)}
.hours-note{left:509px;top:37px;font-size:9.5px}
.hours-table{left:222px;top:51px;width:627px;border-collapse:collapse;color:#fff}
.hours-table td,.hours-table th{height:33px;text-align:left;font-weight:400;font-size:20.5px}
.hours-table th{font-weight:700;font-size:20px}
.hours-table .c1{padding-left:24px;width:230px}
.hours-table .c2{width:209px}
.row-red{background:var(--red)}
.row-orange{background:var(--orange)}

.policies{top:454px;height:176px;width:849px;background:var(--mist)}
.policy-title{font-size:28px;color:var(--red)}
.policy p{font-size:15px;font-weight:300;line-height:20px;color:#333;white-space:nowrap}
.divider{left:423px;top:14px;width:2px;height:150px;background:var(--orange)}

.order{top:630px;height:184px;width:849px;background:var(--cream)}
.sites{right:630px;top:28px;text-align:right;font-size:16.5px;line-height:25.5px}
.tablet{left:232px;top:18px;width:158px;height:108px;background:linear-gradient(160deg,#e6e3da,#cfccc2);border-radius:12px}
.order-title{left:42px;top:128px;font-size:42px;color:var(--olive)}
.zones{left:424px;top:28px;display:grid;grid-template-columns:133px 133px 133px;row-gap:7px;font-size:14px}
.zones .lead{color:var(--red);font-weight:700;font-family:'Roboto Condensed',sans-serif}
.delivery-note{left:428px;top:152px;color:var(--red);font-size:15px}

.services{top:814px;height:168px;width:849px;background:var(--mist)}
.big-label{font-weight:900;color:var(--red);font-size:42px}
.svc{font-size:19.5px;line-height:30px}
.rule{left:256px;top:90px;width:337px;height:2px;background:var(--orange)}

.rules{top:982px;height:144px;width:849px;background:var(--cream)}
.rules-title{left:46px;top:8px;font-size:22px;color:var(--olive)}
.rules-list{left:46px;top:34px;list-style:none;font-size:14.5px;line-height:22.5px}
.rules-list li::before{content:"•";margin-right:9px}
.rules-list .warn{color:var(--red)}
.badge{left:415px;top:16px;width:128px;height:86px;background:var(--red);border-radius:14px;transform:rotate(-20deg)}
.badge-label{left:438px;top:98px;font-size:12px;font-weight:900;color:var(--olive);transform:rotate(-20deg)}
.owner{left:576px;top:38px;font-size:14.5px}
.owner-line{display:flex;align-items:center;gap:10px;font-size:16.5px;margin-top:7px}
.owner-line .icon{width:17px;height:17px;background:var(--olive)}

.warning{top:1126px;height:36px;width:849px;background:var(--red);color:#fff;font-weight:700;font-size:18px;text-align:center;line-height:36px}
.footer{top:1162px;height:38px;width:849px;background:var(--olive);color:#fff;font-weight:700;font-size:18px;text-align:center;line-height:38px}
</style>
</head>
<body>
<div class="sheet">
  <div class="stripe" style="top:0"></div>

  <header class="abs header">
    <div class="abs brand">
      <span class="brand-dot"></span>
      <span class="brand-name">Maple Ridge Indian Restaurant</span>
    </div>
  </header>
  <div class="stripe" style="top:96px"></div>

  <section class="abs location">
    <div class="abs map" role="img" aria-label="Street map showing Maple Ridge Restaurant location"></div>
    <h2 class="abs heading loc-title">Our Location and Contact</h2>
    <div class="abs loc-text">
      Cedar House Pty Ltd T/A Maple Ridge Restaurant<br>
      ABN: 47 208 391 562<br>
      Shop 19-20,<br>
      418 Banksia Parade, Fernvale, WA 6031<br>
      Australia
    </div>
    <div class="abs contact" style="left:413px">
      <span class="icon"><svg width="15" height="15" viewBox="0 0 24 24"><path fill="#fff" d="M6.6 10.8a15 15 0 0 0 6.6 6.6l2.2-2.2c.3-.3.7-.4 1-.2 1.1.4 2.3.6 3.6.6.6 0 1 .4 1 1V20c0 .6-.4 1-1 1A17 17 0 0 1 3 4c0-.6.4-1 1-1h3.5c.6 0 1 .4 1 1 0 1.3.2 2.5.6 3.6.1.3 0 .7-.2 1z"/></svg></span>
      08 9000 4812
    </div>
    <div class="abs contact" style="left:574px">
      <span class="icon"><svg width="16" height="12" viewBox="0 0 16 12"><rect x="1" y="1" width="14" height="10" fill="none" stroke="#fff" stroke-width="1.5"/><path d="M1 1l7 6 7-6" fill="none" stroke="#fff" stroke-width="1.5"/></svg></span>
      admin@mapleridge.com.au
    </div>
  </section>
  <div class="stripe" style="top:296px;height:6px"></div>

  <section class="abs hours">
    <svg class="abs clock" width="140" height="140" viewBox="0 0 140 140">
      <circle cx="70" cy="70" r="63" fill="none" stroke="var(--olive)" stroke-width="10"/>
      <path d="M66 36v38l24 24" fill="none" stroke="var(--olive)" stroke-width="10" stroke-linecap="square"/>
    </svg>
    <h2 class="abs heading hours-title">Opening Hours</h2>
    <div class="abs hours-note">Dinner Buffet is available only from Mon-Thu from 5:30PM-8:30PM</div>
    <table class="abs hours-table">
      <tr class="row-red"><th class="c1"></th><th class="c2">Morning</th><th>Evening</th></tr>
      <tr class="row-orange"><td class="c1">Monday - Friday</td><td class="c2">11:30AM-2:30PM</td><td>5:00PM-9:00PM</td></tr>
      <tr class="row-red"><td class="c1">Saturday &amp; Sunday</td><td class="c2">10:30AM-2:30PM</td><td>5:00PM-9:00PM</td></tr>
    </table>
  </section>

  <section class="abs policies">
    <div class="abs policy" style="left:37px;top:20px;width:380px">
      <h2 class="heading policy-title">Payment Method</h2>
      <p style="margin-top:8px">We accept cash, all Australian debit network,<br>Debit and Credit Cards.</p>
      <p style="margin-top:10px">We accept Crestline, Orbix – A surcharge of 2.8% apply.</p>
      <p style="margin-top:10px">We DO NOT accept Supper Card</p>
    </div>
    <div class="abs divider"></div>
    <div class="abs policy" style="left:452px;top:20px;width:380px">
      <h2 class="heading policy-title">Discount Vouchers</h2>
      <p style="margin-top:8px">We accept Leisure Pass Book Vouchers and<br>Maple Ridge supplied Discount vouchers.</p>
      <p style="margin-top:10px">Leisure Pass Vouchers are eligible only for Dine-In.</p>
    </div>
  </section>

  <section class="abs order">
    <div class="abs sites">www.mapleridge.com.au<br>www.dishdash.com.au<br>www.feedquick.com.au<br>www.platerun.com.au</div>
    <div class="abs tablet" role="img" aria-label="Illustration of a hand tapping a tablet showing a food bowl"></div>
    <h2 class="abs heading order-title">Order Online</h2>
    <div class="abs zones">
      <span class="lead">WE DELIVER TO</span><span>1.Beldon</span><span>2.Craigie</span>
      <span>3.Darch</span><span>4.Duncraig</span><span>5.Edgewater</span>
      <span>6.Greenwood</span><span>7.Hocking</span><span>8.Kingsley</span>
      <span>9.Madeley</span><span>10.Padbury</span><span>11.Pearsall</span>
      <span>12.Wangara</span><span>13.Woodvale</span><span></span>
    </div>
    <div class="abs delivery-note">Delivery Charges $5 and minimum order value $30</div>
  </section>

  <section class="abs services">
    <div class="abs big-label" style="left:40px;top:8px">SERVICES</div>
    <div class="abs svc" style="left:69px;top:63px">Business Meetings</div>
    <div class="abs svc" style="left:290px;top:3px">Functions/Parties<br>Catering<br>Seminars/Presentations</div>
    <div class="abs svc" style="left:621px;top:3px">Bulk Cooking<br>Special Orders<br>Party Orders</div>
    <div class="abs rule"></div>
    <div class="abs big-label" style="left:46px;top:95px">FACILITIES</div>
    <div class="abs svc" style="left:68px;top:133px">Baby changer table</div>
    <div class="abs svc" style="left:289px;top:103px">Wheel chair access<br>High rise tables for babies</div>
    <div class="abs svc" style="left:620px;top:103px">Disabled toilet inside<br>Music system</div>
  </section>

  <section class="abs rules">
    <h2 class="abs heading rules-title">House Rules &amp; BYO</h2>
    <ul class="abs rules-list">
      <li>Prices are inclusive of GST</li>
      <li>Prices are subject to change without notice</li>
      <li style="line-height:16px;padding-top:3px">Outside Food and Beverages (except WINE)<br>&nbsp;&nbsp;&nbsp;are not allowed</li>
      <li class="warn" style="margin-top:4px">BYO allowed – only for Wine . Charges per bottle apply</li>
    </ul>
    <div class="abs badge" role="img" aria-label="ID card illustration for new management"></div>
    <div class="abs badge-label">NEW MANAGEMENT</div>
    <div class="abs owner">
      Restaurant Owner : Rina Dalvi
      <div class="owner-line"><span class="icon"></span>0400123456</div>
      <div class="owner-line" style="margin-top:10px"><span class="icon"></span>rina@mapleridge.com.au</div>
    </div>
  </section>

  <div class="abs warning">WARNING Please inform wait staff for any allergies. Food consumed at your own risk.</div>
  <div class="abs footer">Please visit www.mapleridge.com.au to book your table or contact us on 08 9000 4812</div>
</div>
</body>
</html>
```